Cat-products company needs smart, yet endearing, business card

We need a business card design for a new, but up-and-running, business based in Honolulu, Hawaii. The business is Purrlane Nest Co. Our first product is the most environmentally-friendly cat grass kit ever seen on the planet. Future products, currently in the R&D phase, will include a variety of exciting cat scratchers. We also do consulting work to help apartment-dwellers make their home more cat-friendly and, in the future, plan on doing full, custom installs of structure to create high walkways for cats.

Target Market(s)

Middle-aged, apartment-dwelling, middle-class workers who own 1 or more cats and who dote on them.

Industry/Entity Type

Pet Care

Contact Information for Business Card

A striking, professional, yet warm and friendly design is what we're after.

Font styles to use
Serif
Sans Serif
Other font styles liked:
• Comfortaa

Colors

Designer to choose colors to be used in the design.

Requirements
Must have
• The company logo: (see attachment)
• The company name: Purrlane Nest Co
• The web address: www.purrlanenestco.example
• Email: support@purrlanenestco.example
• Phone: +1 (808) 555 0172
• Update (Fri Jun 30 3017 7:45pm Hawaii Time) I would like, is possible, uploaded picture of the cat grass kit on the back of the card with some text along the lines of: Purrlane Nest Co - Where The Freshest Kitty Sprouts Begin
Nice to have
• A cat picture, cartoon, real or silhouette that illustrates cats in action and/or relaxing; ie using the apartment space to live, play and relax in and being well-contented.
• Most of the website is done in the font: Comfortaa. It might be nice to continue using this for brand consistency.
Should not have
• Hard-to-read fonts.

```html
<!DOCTYPE html>
<html lang="en">
<head>
<meta charset="utf-8">
<title>Purrlane Nest Co — Business Card</title>
<link href="https://fonts.googleapis.com/css2?family=Comfortaa:wght@300;400;700&display=swap" rel="stylesheet">
<style>
  :root {
    --backdrop: #f3b1c3;
    --rose: #d7667c;
    --paper: #f1f0ee;
    --teal: #45bccb;
    --teal-soft: #bfe5ea;
    --rose-soft: #f2cdd5;
    --cocoa: #5a2b24;
    --white: #ffffff;
  }
  * { margin: 0; padding: 0; box-sizing: border-box; }
  html, body { width: 1200px; height: 900px; overflow: hidden; }
  body {
    background: var(--backdrop);
    font-family: 'Comfortaa', sans-serif;
    position: relative;
  }
  .card {
    position: absolute;
    left: 320px;
    width: 560px;
    height: 320px;
    overflow: hidden;
    box-shadow: 0 6px 18px rgba(120, 40, 60, 0.18);
  }
  .card--front { top: 100px; background: var(--rose); }
  .card--back { top: 480px; background: var(--paper); }
  .card__shape { position: absolute; inset: 0; width: 100%; height: 100%; }

  .brand {
    position: absolute;
    left: 180px;
    top: 112px;
    width: 280px;
    display: flex;
    align-items: center;
    gap: 14px;
  }
  .brand__dot {
    width: 40px; height: 40px;
    border-radius: 50%;
    background: var(--cocoa);
    flex: none;
  }
  .brand__name {
    font-weight: 700;
    font-size: 30px;
    line-height: 1.1;
    color: var(--teal);
  }

  .contact {
    position: absolute;
    left: 36px;
    top: 112px;
    color: var(--white);
  }
  .contact__name {
    font-weight: 300;
    font-size: 36px;
    line-height: 1.12;
    margin-bottom: 18px;
    letter-spacing: 0.5px;
  }
  .contact__line {
    font-weight: 300;
    font-size: 12px;
    line-height: 1.75;
    letter-spacing: 0.6px;
  }
  .cat-art {
    position: absolute;
    left: 300px;
    top: 14px;
    width: 240px;
    height: 170px;
    border-radius: 24px;
    background: linear-gradient(135deg, var(--teal-soft) 0%, var(--paper) 50%, var(--rose-soft) 100%);
  }
</style>
</head>
<body>

  <section class="card card--front" aria-label="Card front">
    <svg class="card__shape" viewBox="0 0 560 320" preserveAspectRatio="none" aria-hidden="true">
      <path d="M165 0 L430 0 C500 30 540 90 540 150 C540 220 470 275 400 320 L225 320 C175 290 145 240 150 190 C156 130 140 60 165 0 Z" fill="var(--paper)"/>
    </svg>
    <div class="brand">
      <span class="brand__dot"></span>
      <span class="brand__name">Purrlane<br>Nest Co</span>
    </div>
  </section>

  <section class="card card--back" aria-label="Card back">
    <svg class="card__shape" viewBox="0 0 560 320" preserveAspectRatio="none" aria-hidden="true">
      <path d="M0 70 L230 70 C300 70 330 150 380 200 C420 240 480 250 560 250 L560 320 L0 320 Z" fill="var(--rose)"/>
      <path d="M0 76 L228 76 C294 76 322 156 372 206 C412 246 478 256 560 256 L560 320 L0 320 Z" fill="var(--teal)"/>
    </svg>
    <div class="cat-art" role="img" aria-label="Illustration of a white cat face with blue eyes, whiskers and a pink nose"></div>
    <div class="contact">
      <h1 class="contact__name">Purrlane<br>Nest Co</h1>
      <p class="contact__line">www.purrlanenestco.example</p>
      <p class="contact__line">support@purrlanenestco.example</p>
      <p class="contact__line">+1 (808) 555 0172</p>
    </div>
  </section>

</body>
</html>
```